Brookvane Counsel Partners Website Design

I need a website design for my new business consulting and executive coaching firm, Brookvane Counsel Partners. We provide consultative services to business C-suites as well as personal coaching to executives. I have attached the logo with color scheme I have chosen. I would like the website to reflect professionalism and continue the color scheme in the logo.

Target Market(s)

Small to medium business and their executives; middle to upper income men and women in mid- to late career looking for significance

Industry/Entity Type

Business Consultant

Number of Pages Required

4 page

Requirements
Must have
• A homepage with prominent logo and way to contact for more information; an area on the homepage with easy to read, clear text to describe what the company does; a prominent area on the homepage for a tagline; a blog page that can be updated regularly, an "about us" page with biographical information; an "about us" page; a page detailing services offered
• The web design must match the logo colors and font that I have uploaded.
Nice to have
• A lighthouse picture in the background or header
Should not have
• A lot of text area on the homepage

```html
<!DOCTYPE html>
<html lang="en">
<head>
<meta charset="utf-8">
<title>Brookvane Counsel Partners</title>
<link href="https://fonts.googleapis.com/css2?family=Cinzel:wght@400;700&family=Arimo:wght@400;700&display=swap" rel="stylesheet">
<style>
:root{
  --linen:#e9e5da;
  --linen-dark:#dcd6c8;
  --crimson:#7a1418;
  --crimson-dark:#5c0e11;
  --navy:#1c2a5e;
  --navy-dark:#14204a;
  --ink:#333333;
  --muted:#8a8a8a;
  --white:#ffffff;
  --panel:#f7f6f3;
  --sky:#2b8fd0;
  --sky-dark:#1a6aa6;
}
*{box-sizing:border-box;margin:0;padding:0}
html,body{width:1200px;height:1021px;overflow:hidden}
body{
  position:relative;
  background:var(--linen) repeating-linear-gradient(45deg,rgba(255,255,255,.12) 0 2px,transparent 2px 5px);
  font-family:"Arimo",Arial,sans-serif;color:var(--ink);
}
.serif{font-family:"Cinzel",Georgia,serif}

.header-band{position:absolute;left:0;top:76px;width:1200px;height:50px;background:var(--crimson);
  border-top:2px solid var(--crimson-dark);border-bottom:2px solid var(--crimson-dark);
  box-shadow:inset 0 2px 0 rgba(255,255,255,.25),inset 0 -2px 0 rgba(255,255,255,.25)}
.logo-card{position:absolute;left:128px;top:30px;width:239px;height:108px;background:var(--white);
  box-shadow:0 3px 6px rgba(0,0,0,.35);display:flex;align-items:center;justify-content:center;gap:8px}
.logo-mark{width:26px;height:26px;background:var(--crimson)}
.logo-name{font-family:"Cinzel",Georgia,serif;font-weight:700;color:var(--navy);font-size:15px;line-height:1.15;width:170px}
.contact-line{position:absolute;right:132px;top:33px;font-family:"Cinzel",Georgia,serif;color:var(--crimson);font-size:21px}
.main-nav{position:absolute;right:131px;top:91px;display:flex;gap:46px}
.main-nav a{font-family:"Cinzel",Georgia,serif;color:var(--white);text-decoration:none;font-size:16px}

.hero{position:absolute;left:128px;top:160px;width:943px;height:299px;
  background:linear-gradient(180deg,#1e355e 0%,#3f5f8c 55%,#6f8fb5 100%);box-shadow:0 6px 8px rgba(0,0,0,.25)}
.slide-arrow{position:absolute;top:126px;width:33px;height:33px;border-radius:50%;background:#e6e3df;
  display:flex;align-items:center;justify-content:center;box-shadow:0 1px 3px rgba(0,0,0,.4)}
.slide-arrow.prev{left:8px}.slide-arrow.next{right:8px}

.tagline-bar{position:absolute;left:128px;top:481px;width:943px;height:65px;border-radius:10px;
  background:linear-gradient(90deg,#f3f3f4,#ffffff 60%,#f0f0f2)}
.tagline-bar h1{position:absolute;left:16px;top:6px;font-family:"Cinzel",Georgia,serif;font-weight:400;
  color:var(--navy);font-size:21px;line-height:25px}
.cta{position:absolute;left:670px;top:10px;width:252px;height:47px;border-radius:4px;
  background:linear-gradient(180deg,var(--sky),var(--sky-dark));display:flex;align-items:center;color:var(--white);
  font-family:"Arimo",Arial,sans-serif;font-weight:700;font-size:23px;text-decoration:none}
.cta svg{margin:0 10px 0 12px}
.cta span{border-left:1px solid rgba(255,255,255,.35);padding-left:12px}

.card{position:absolute;top:586px;width:303px;height:306px;background:var(--panel);box-shadow:0 1px 3px rgba(0,0,0,.2)}
.card.welcome{left:128px}.card.blog{left:449px}.card.inquiry{left:768px}
.card-title{position:absolute;left:20px;top:-5px;width:170px;height:34px;background:var(--navy);border-radius:0 0 4px 4px;
  color:var(--white);font-family:"Cinzel",Georgia,serif;font-size:17px;text-align:center;line-height:34px}
.photo{position:absolute;background:linear-gradient(135deg,#8fa8a0,#c9d3d0 50%,#4a5a66)}
.welcome .photo{left:14px;top:37px;width:273px;height:141px}
.welcome p{position:absolute;left:15px;top:184px;width:275px;font-size:14px;line-height:20px}
.pill{position:absolute;bottom:-5px;height:27px;padding:0 13px;background:var(--crimson);color:var(--white);
  border-radius:5px 5px 0 0;font-size:14px;line-height:27px;text-decoration:none}
.welcome .pill,.blog .pill{right:14px}
.post{position:absolute;left:12px;width:285px;height:98px}
.post .photo{left:0;top:0;width:114px;height:96px;border:1px solid #ccc;background:linear-gradient(180deg,#5b7ea8,#6c6b55 60%,#3e5a2e)}
.post h3{position:absolute;left:128px;top:2px;font-weight:400;font-size:15px;color:#444}
.post .date{position:absolute;left:128px;top:22px;font-size:14px;color:var(--crimson)}
.post p{position:absolute;left:129px;top:41px;width:160px;font-size:14px;line-height:19px}
.post .more{color:var(--muted)}
.post-divider{position:absolute;left:20px;top:156px;width:263px;border-top:1px dotted #aaa}
.field{position:absolute;left:15px;width:286px;background:var(--white);border:1px solid #ddd;
  font-size:12px;color:#666;padding-left:30px;line-height:33px}
.field svg{position:absolute;left:9px;top:10px}
.inquiry .pill{right:16px;padding:0 22px}

.footer{position:absolute;left:0;top:946px;width:1200px;height:75px;background:var(--navy);border-top:6px solid var(--crimson)}
.footer-nav{position:absolute;left:140px;top:11px;font-size:13px;color:var(--white)}
.footer-nav a{color:var(--white);text-decoration:none}
.footer-nav .sep{margin:0 9px}
.copyright{position:absolute;left:141px;top:42px;font-size:13px;color:var(--white)}
.footer-mark{position:absolute;left:601px;top:14px;width:38px;height:38px;border-radius:50%;background:var(--navy-dark)}
.follow{position:absolute;left:838px;top:24px;display:flex;align-items:center;gap:8px;color:var(--white);font-size:16px}
.follow span{margin-right:4px}
.social{width:30px;height:30px;border-radius:50%;background:var(--white)}
</style>
</head>
<body>
<header>
  <div class="header-band"></div>
  <div class="logo-card"><div class="logo-mark"></div><div class="logo-name">Brookvane Counsel Partners</div></div>
  <div class="contact-line">Contact us Today : 555-014-2290</div>
  <nav class="main-nav"><a href="#">Home</a><a href="#">About Us</a><a href="#">Services</a><a href="#">Blog</a><a href="#">Contact Us</a></nav>
</header>

<section class="hero" role="img" aria-label="Businessman in a suit facing a chalkboard sketch of charts, ideas and success diagrams">
  <span class="slide-arrow prev"><svg width="10" height="14" viewBox="0 0 10 14"><path d="M8 1L2 7l6 6" stroke="#7a1418" stroke-width="3" fill="none"/></svg></span>
  <span class="slide-arrow next"><svg width="10" height="14" viewBox="0 0 10 14"><path d="M2 1l6 6-6 6" stroke="#333" stroke-width="3" fill="none"/></svg></span>
</section>

<section class="tagline-bar">
  <h1>We Are A Firm Providing Services Are<br>Business Consulting &amp; Executive Coaching</h1>
  <a class="cta" href="#"><svg width="28" height="32" viewBox="0 0 28 32"><path d="M2 10h12V2l12 14-12 14v-8H2z" fill="#1c2a5e" stroke="#fff" stroke-width="2"/></svg><span>Get Started Now!</span></a>
</section>

<section class="card welcome">
  <div class="card-title">Welcome to BCP</div>
  <div class="photo" role="img" aria-label="Smiling businesswoman in an office corridor"></div>
  <p>Lorem ipsum dolor sit amet, consectetuer adipiscing elit, sed diam nonumibh euismod tcidunt ut laoreet dolore magna aliquam erat volutpat. Ut wisi enim ad minim veniam, quis nostrud exerci tation.</p>
  <a class="pill" href="#">Read More</a>
</section>

<section class="card blog">
  <div class="card-title">Blog Posts</div>
  <article class="post" style="top:40px">
    <div class="photo" role="img" aria-label="Two-storey family house with trees"></div>
    <h3>Ut tellus dolor dapib</h3><div class="date">01.01.2016</div>
    <p>Utm tellus doloribus eget, elemen velmki cursu itas. Aenean auctorbbni <span class="more">[...]</span></p>
  </article>
  <div class="post-divider"></div>
  <article class="post" style="top:176px">
    <div class="photo" role="img" aria-label="Two-storey family house with trees"></div>
    <h3>Ut tellus dolor dapib</h3><div class="date">01.01.2016</div>
    <p>Utm tellus doloribus eget, elemen velmki cursu itas. Aenean auctorbbni <span class="more">[...]</span></p>
  </article>
  <a class="pill" href="#">Read More</a>
</section>

<section class="card inquiry">
  <div class="card-title">Quick Inquiry</div>
  <div class="field" style="top:45px;height:35px"><svg width="13" height="13" viewBox="0 0 13 13"><circle cx="6.5" cy="4" r="3" fill="#999"/><path d="M1 13c0-4 2.5-5.5 5.5-5.5S12 9 12 13z" fill="#999"/></svg>Name</div>
  <div class="field" style="top:86px;height:35px"><svg width="14" height="11" viewBox="0 0 14 11"><rect x=".5" y=".5" width="13" height="10" fill="none" stroke="#999"/><path d="M.5.5l6.5 6 6.5-6" fill="none" stroke="#999"/></svg>Email</div>
  <div class="field" style="top:127px;height:145px"><svg width="14" height="14" viewBox="0 0 14 14"><rect x=".5" y="2.5" width="11" height="11" fill="none" stroke="#999"/><path d="M5 9l1-3 7-6 1 1-7 6z" fill="#999"/></svg>Message</div>
  <a class="pill" href="#">Submit</a>
</section>

<footer class="footer">
  <nav class="footer-nav"><a href="#">Home</a><span class="sep">|</span><a href="#">About Us</a><span class="sep">|</span><a href="#">Services</a><span class="sep">|</span><a href="#">Blog</a><span class="sep">|</span><a href="#">Contact Us</a></nav>
  <div class="copyright">© 2016 Brookvane Counsel Partners All Rights Reserved</div>
  <div class="footer-mark"></div>
  <div class="follow"><span>FOLLOW US</span><a class="social" href="#" aria-label="Social profile"></a><a class="social" href="#" aria-label="Social profile"></a><a class="social" href="#" aria-label="Social profile"></a><a class="social" href="#" aria-label="Social profile"></a></div>
</footer>
</body>
</html>
```